KW Sports & Remedial Massage needs a new logo & business card design

The design is for my Sports and remedial massage business. My business is aimed at everyone who has a muscle ache or injury so not just sports related. I need a design which is sharp, clear and professional. No greens, or pastel colours or floral/girly designs. Perhaps just a Navy background and white text or other way around or perhaps grey. I want to make it clear that I treat everyone and not just sporty people.

Target Market(s)

People with muscle aches or sports injuries

Industry/Entity Type

Health And Wellness

Contact Information for Business Card

It needs to also include the following:
Name: Marion Kebbell
Mobile No: 07432 519 268
Email: marionkebbell@postvane.com
Qualifications: Dip SM, Dip SRM

Logo Text

KW Sports & Remedial Massage

Font styles to use
Serif
Other font styles liked:
• Tahoma, Verdana

Colors
5c5c5c
7f7f7f
9d9d9d
0255a3
3176b5
85abd2

Requirements
Must have
• I was thinking of a few simple people figures at the bottom of the card to highlight this i.e. a gardener, musician mixed in with a cyclist and tennis player.
Should not have
• Anything which indicates beauty therapy or relaxing. I am there to get rid of aches and pains and often to give rehab to certain injuries.

```html
<!DOCTYPE html>
<html lang="en">
<head>
<meta charset="utf-8">
<title>KW Sports &amp; Remedial Massage – Business Card</title>
<link rel="stylesheet" href="https://fonts.googleapis.com/css2?family=Marcellus&family=Open+Sans:wght@400&display=swap">
<style>
  :root {
    --canvas: #d9d9d9;
    --card-black: #000000;
    --card-white: #ffffff;
    --brand-blue: #1ba1d8;
    --brand-grey: #8a8c8e;
    --text-grey: #c8c8c8;
  }
  * { margin: 0; padding: 0; box-sizing: border-box; }
  html, body {
    width: 1200px; height: 900px; overflow: hidden;
    background: var(--canvas);
  }
  .stage {
    position: relative; width: 1200px; height: 900px;
    display: flex; align-items: center; justify-content: center; gap: 50px;
  }
  .card {
    position: relative; width: 540px; height: 309px;
    overflow: hidden;
    box-shadow: 0 2px 6px rgba(0,0,0,.25);
  }
  .card--front {
    background: var(--card-black);
    display: flex; align-items: center; justify-content: center;
  }
  .brand-name {
    font-family: "Marcellus", Georgia, serif;
    color: var(--brand-blue);
    font-size: 27px;
    letter-spacing: 1px;
    display: flex; align-items: center; gap: 12px;
  }
  .brand-name__dot {
    width: 14px; height: 14px; border-radius: 50%;
    background: var(--brand-blue);
  }
  .card--back { background: var(--card-white); }
  .card__curve { position: absolute; inset: 0; }
  .contact {
    position: absolute; left: 34px; top: 44px;
  }
  .contact__brand {
    font-family: "Marcellus", Georgia, serif;
    color: var(--brand-grey);
    font-size: 15px; letter-spacing: .5px;
    margin-bottom: 58px;
  }
  .contact__name {
    font-family: "Marcellus", Georgia, serif;
    font-weight: 400;
    color: var(--brand-blue);
    font-size: 27px; line-height: 1;
  }
  .contact__quals {
    font-family: "Open Sans", Tahoma, sans-serif;
    color: var(--text-grey);
    font-size: 13px; margin-top: 6px; margin-bottom: 18px;
  }
  .contact__line {
    font-family: "Open Sans", Tahoma, sans-serif;
    color: var(--text-grey);
    font-size: 15px; display: flex; align-items: center; gap: 8px;
    margin-bottom: 5px; white-space: nowrap;
  }
  .contact__icon { width: 12px; height: 12px; flex: none; }
</style>
</head>
<body>
<main class="stage">
  <section class="card card--front" aria-label="Business card front">
    <div class="brand-name"><span class="brand-name__dot"></span>KW Sports &amp; Remedial Massage</div>
  </section>

  <section class="card card--back" aria-label="Business card back">
    <svg class="card__curve" viewBox="0 0 540 309" width="540" height="309" aria-hidden="true">
      <path d="M0 0 H352 C414 100 398 232 272 309 H0 Z" fill="var(--brand-grey)"/>
      <path d="M0 0 H340 C402 108 394 226 264 309 H0 Z" fill="var(--brand-blue)"/>
      <path d="M0 0 H332 C392 100 382 220 250 309 H0 Z" fill="var(--card-black)"/>
    </svg>
    <div class="contact">
      <p class="contact__brand">KW Sports &amp; Remedial Massage</p>
      <h1 class="contact__name">Marion Kebbell</h1>
      <p class="contact__quals">Dip SM, Dip SRM</p>
      <p class="contact__line">
        <svg class="contact__icon" viewBox="0 0 12 12" aria-hidden="true"><path d="M1 3 C1 1.5 2 1 6 1 C10 1 11 1.5 11 3 L9 4 L8 3 H4 L3 4 Z M3 5 H9 L10 11 H2 Z" fill="var(--brand-blue)"/></svg>
        07432 519 268
      </p>
      <p class="contact__line">
        <svg class="contact__icon" viewBox="0 0 12 12" aria-hidden="true"><rect x="0.5" y="2" width="11" height="8" fill="var(--brand-blue)"/><path d="M0.5 2 L6 7 L11.5 2" stroke="#000" stroke-width="1" fill="none"/></svg>
        marionkebbell@postvane.com
      </p>
    </div>
  </section>
</main>
</body>
</html>
```